Consulting company needs Business Cards - rough concept provided

I'm looking for someone to take our business card idea and make is slick and polished - to communicate our high-end, sophisticated, serious consulting business. We have a rough layout we did in-house. We are open to ideas on repo-ing elements, adjusting sizes, typefaces etc... within the general concept we've already come up with. We want it to be super-clean and sophisticated. We want to keep the white backgrounds, and blue brand colors. Our goal is to print with painted blue edges on thick cardstock. Thank you!!

```html
<!DOCTYPE html>
<html lang="en">
<head>
<meta charset="utf-8">
<title>Halvern Stationery</title>
<link rel="stylesheet" href="https://fonts.googleapis.com/css2?family=Ubuntu:wght@400;500;700&family=Open+Sans:wght@400;600&display=swap">
<style>
  :root {
    --brand-blue: #1f8bd6;
    --paper: #ffffff;
    --backdrop: #ebe9e6;
    --ink: #2b2b2b;
    --ink-soft: #7a7d80;
    --rule-grey: #c9cbcd;
    --panel-grey: #d9dadb;
  }
  * { box-sizing: border-box; margin: 0; padding: 0; }
  html, body { width: 1200px; height: 807px; overflow: hidden; }
  body { background: var(--backdrop); font-family: "Open Sans", sans-serif; color: var(--ink); }
  .canvas { position: relative; width: 1200px; height: 807px; }
  .sheet { position: absolute; background: var(--paper); overflow: hidden; box-shadow: 0 2px 6px rgba(0,0,0,.12); }
  .sheet svg.art { position: absolute; inset: 0; }
  .wordmark { position: absolute; font-family: "Ubuntu", sans-serif; font-weight: 700; color: var(--brand-blue); letter-spacing: .02em; line-height: 1; }
  .small-text { position: absolute; font-size: 9.5px; line-height: 1.35; color: var(--ink); }

  /* DL envelope front */
  .envelope-front { left: 28px; top: 35px; width: 576px; height: 241px; }
  .envelope-front .wordmark { left: 405px; top: 22px; font-size: 30px; }
  .envelope-front .sender { left: 405px; top: 62px; }
  .envelope-front .contact { left: 470px; top: 214px; font-size: 8.5px; }
  .line-field { position: absolute; left: 0; top: 30px; width: 330px; height: 211px;
    background: linear-gradient(160deg, #f1f2f3, #fafafa); }

  /* Letterhead */
  .letterhead { left: 687px; top: 35px; width: 501px; height: 263px; box-shadow: none; }
  .letterhead .wordmark { right: 62px; top: 24px; font-size: 32px; }
  .letterhead .header-rule { position: absolute; left: 0; top: 64px; width: 441px; height: 1.5px; background: var(--brand-blue); }
  .letterhead .recipient { left: 68px; top: 162px; font-size: 8px; }
  .letterhead .greeting { left: 68px; top: 203px; font-size: 8px; }
  .letterhead .body-copy { left: 68px; top: 218px; width: 380px; font-size: 7.5px; }
  .letterhead .body-copy p + p { margin-top: 6px; }

  /* Painted card edges */
  .card-edges { position: absolute; left: 15px; top: 353px; width: 107px; height: 434px;
    background: repeating-linear-gradient(90deg, #1f8bd6 0 3px, #2a95de 3px 4px); box-shadow: 0 2px 6px rgba(0,0,0,.15); }

  /* Business cards */
  .card-front { left: 179px; top: 353px; width: 281px; height: 180px; }
  .card-back { left: 179px; top: 578px; width: 281px; height: 180px; }
  .card-back .wordmark { left: 14px; top: 26px; font-size: 27px; }
  .card-back .card-rule { position: absolute; left: 89px; top: 68px; width: 192px; height: 1.5px; background: var(--brand-blue); }
  .card-back .card-contact { left: 89px; top: 82px; font-size: 10px; }

  /* Envelope back */
  .envelope-back { left: 518px; top: 349px; width: 649px; height: 409px; }
  .envelope-back .return-address { position: absolute; left: 69px; top: 336px; font-size: 12.5px; line-height: 1.4; color: var(--ink-soft); }
</style>
</head>
<body>
<main class="canvas">

  <section class="sheet envelope-front" aria-label="DL envelope">
    <div class="line-field" role="img" aria-label="Fine-line geometric decoration"></div>
    <svg class="art" width="576" height="241" viewBox="0 0 576 241">
      <rect x="395" y="0" width="181" height="10" fill="var(--brand-blue)"/>
      <line x1="356" y1="0" x2="452" y2="241" stroke="var(--brand-blue)" stroke-width="1.2"/>
      <polygon points="436,192 576,192 576,241 452,241" fill="var(--panel-grey)" role="img" aria-label="Grey grid panel"/>
      <circle cx="520" cy="122" r="30" fill="none" stroke="var(--rule-grey)" stroke-width="1.2"/>
    </svg>
    <div class="wordmark">HALVERN</div>
    <div class="small-text sender">Company Address<br>&nbsp;&nbsp;48 Ardent Lane<br>&nbsp;&nbsp;Marlow Bay, USA</div>
    <div class="small-text contact">+1 555 014 2290<br>office@halvern.com</div>
  </section>

  <section class="sheet letterhead" aria-label="Letterhead">
    <div class="wordmark">HALVERN</div>
    <div class="header-rule"></div>
    <div class="small-text recipient">Recipient Address<br>48 Ardent Lane<br>Company | USA</div>
    <div class="small-text greeting">Dear Morgan,</div>
    <div class="small-text body-copy">
      <p>Lorem ipsum dolor sit amet, consectetur adipiscing elit, sed do eiusmod tempor incididunt ut labore et dolore magna aliqua. Ut enim ad minim veniam, quis nostrud exercitation ullamco laboris nisi ut aliquip ex ea commodo consequat.</p>
      <p>Duis aute irure dolor in reprehenderit in voluptate velit esse cillum dolore eu fugiat nulla pariatur. Excepteur sint occaecat cupidatat non proident.</p>
    </div>
  </section>

  <div class="card-edges" aria-label="Painted blue card edges"></div>

  <section class="sheet card-front" aria-label="Business card front">
    <svg class="art" width="281" height="180" viewBox="0 0 281 180">
      <polygon points="28,28 50,28 28,54" fill="var(--brand-blue)"/>
      <polygon points="245,0 281,0 281,180 203,180" fill="var(--brand-blue)"/>
    </svg>
  </section>

  <section class="sheet card-back" aria-label="Business card back">
    <div class="wordmark">HALVERN</div>
    <div class="card-rule"></div>
    <div class="small-text card-contact">Contact info<br>+1 555 014 2291<br>hello@halvern.com<br>www.halvern.com</div>
  </section>

  <section class="sheet envelope-back" aria-label="Envelope back">
    <svg class="art" width="649" height="409" viewBox="0 0 649 409">
      <polygon points="0,0 649,0 649,85 305,158 0,17" fill="#f7f7f7" stroke="#dcdcdc" stroke-width="1"/>
      <polygon points="356,0 649,0 649,85 305,158" fill="var(--brand-blue)"/>
    </svg>
    <div class="return-address">If undelivered<br>48 Ardent Lane<br>Company , USA</div>
  </section>

</main>
</body>
</html>
```